Paper Towel Design - comparable to Plumrix, Toldex, Wendrove, Quor

1.I needed a design for a new product, PAPER TOWEL
2. Name: MARVOLIN (Trademark)
3. One word with letters TM for a trademark at the end of the name
4. Include: SNIP-N-FOLD this pertains to sheet size of 11 inches x 6 inches
5. Include: 100 percent biodegradable
6. Include: STRONG & ABSORBENT
7. Include the words Paper Towel

Hoxley Market(s)

Household, store, businesses (Online, Fennick, Brulio, Hoxley)

Industry/Entity Type

Paper Product

Font styles to use
Script

Colors
6b449b
33a6d7
fbee3e

Requirements
Must have
• vibrant color - striking design
Nice to have
• Excellent color combination of cyan, yellow, and purple
Should not have
• Should not be suggestive of any similar product, it should be unique and has its own identity

```html
<!DOCTYPE html>
<html lang="en">
<head>
<meta charset="utf-8">
<title>MARVOLIN Paper Towel</title>
<link rel="stylesheet" href="https://fonts.googleapis.com/css2?family=Fira+Sans+Extra+Condensed:wght@600;700&family=Lilita+One&display=swap">
<style>
  :root {
    --purple: #6b449b;
    --cyan: #7fcbe8;
    --cyan-deep: #33a6d7;
    --yellow: #fbee3e;
    --yellow-deep: #c9bd2a;
    --glow: #fdfbc4;
    --mint: #b9e3dc;
    --sky: #86cbe6;
  }
  html, body {
    margin: 0;
    padding: 0;
    width: 1200px;
    height: 1200px;
    overflow: hidden;
    background: #ffffff;
  }
  .package-face {
    display: block;
    width: 1200px;
    height: 1200px;
  }
  .condensed {
    font-family: "Fira Sans Extra Condensed", "Arial Narrow", sans-serif;
    font-weight: 700;
  }
  .display {
    font-family: "Lilita One", "Arial Black", sans-serif;
  }
  .eco-claim { fill: var(--cyan); font-size: 66px; }
  .size-name { fill: var(--purple); font-size: 112px; }
  .size-number {
    fill: var(--yellow);
    stroke: var(--cyan);
    stroke-width: 10px;
    paint-order: stroke;
    font-size: 200px;
  }
  .size-times { font-size: 120px; }
  .brand-name {
    fill: var(--purple);
    stroke: var(--yellow);
    stroke-width: 16px;
    stroke-linejoin: round;
    paint-order: stroke;
    font-size: 270px;
  }
  .tagline { fill: var(--yellow); font-size: 82px; }
  .product-type {
    fill: var(--yellow);
    stroke: var(--purple);
    stroke-width: 16px;
    stroke-linejoin: round;
    paint-order: stroke;
    font-size: 170px;
  }
  .ribbon-text { fill: var(--purple); font-size: 66px; }
</style>
</head>
<body>
<svg class="package-face" viewBox="0 0 1400 1400" xmlns="http://www.w3.org/2000/svg">
  <defs>
    <radialGradient id="bg-glow" cx="0.42" cy="0.46" r="0.75">
      <stop offset="0" stop-color="var(--glow)"/>
      <stop offset="0.3" stop-color="#f3f6b0"/>
      <stop offset="0.6" stop-color="var(--mint)"/>
      <stop offset="1" stop-color="var(--sky)"/>
    </radialGradient>
    <linearGradient id="tagline-band" x1="0" y1="0" x2="1" y2="0">
      <stop offset="0" stop-color="#6b449b" stop-opacity="0.15"/>
      <stop offset="0.35" stop-color="#6b449b" stop-opacity="0.75"/>
      <stop offset="1" stop-color="#6b449b" stop-opacity="0.35"/>
    </linearGradient>
  </defs>

  <rect class="background" width="1400" height="1400" fill="url(#bg-glow)"/>

  <!-- Eco band -->
  <polygon class="eco-band" points="0,180 720,0 1230,0 0,345" fill="var(--purple)"/>
  <g transform="translate(128,215) rotate(-17)">
    <text class="eco-claim condensed" x="0" y="0">100 PERCENT</text>
  </g>
  <g transform="translate(318,232) rotate(-17)">
    <text class="eco-claim condensed" x="0" y="0">BIODEGRADABLE</text>
  </g>

  <!-- Sheet size band -->
  <g class="size-band" transform="translate(0,552) rotate(-17)">
    <rect x="-40" y="-82" width="1030" height="164" fill="var(--cyan)"/>
    <rect x="600" y="-165" width="345" height="200" rx="34" fill="var(--cyan)"/>
    <text class="size-name condensed" x="88" y="46">SNIP-N-FOLD</text>
    <text class="size-number condensed" x="622" y="22">11<tspan class="size-times">x</tspan>6</text>
  </g>

  <!-- Brand name -->
  <g transform="translate(98,905) rotate(-20)">
    <text class="brand-name display" x="0" y="0" textLength="1300" lengthAdjust="spacingAndGlyphs">MARVOLIN</text>
  </g>

  <!-- Tagline -->
  <g transform="translate(335,968) rotate(-16)">
    <rect x="0" y="-92" width="860" height="112" fill="url(#tagline-band)"/>
    <text class="tagline condensed" x="110" y="0" textLength="630" lengthAdjust="spacingAndGlyphs">TOUGH MESS, NO MORE</text>
  </g>

  <!-- Product type -->
  <g transform="translate(398,1142) rotate(-18)">
    <text class="product-type display" x="0" y="0" textLength="820" lengthAdjust="spacingAndGlyphs">PAPER TOWEL</text>
  </g>

  <!-- Strength ribbon -->
  <polygon class="ribbon-tail" points="1110,1296 1238,1300 1112,1366" fill="var(--yellow-deep)"/>
  <polygon class="ribbon" points="920,1180 1282,1086 1364,1262 958,1306" fill="var(--yellow)"/>
  <g transform="translate(982,1228) rotate(-15)">
    <text class="ribbon-text condensed" x="0" y="0">STRONG AND</text>
  </g>
  <g transform="translate(1008,1282) rotate(-15)">
    <text class="ribbon-text condensed" x="0" y="0">ABSORBENT</text>
  </g>
</svg>
</body>
</html>
```